Business card for a boutique travel agency VELIRANDE

we need a business card design - double sided. We would like to have a very elegant, sophisticated but modern design. we are travel consultants and our business focus is Europe, mainly the city of Paris. We would like to receive designs in white and silver, black color but if you are confident that we should pick up a color to make it different and more beautful...go ahead! We are going to give business cards to our clients and business partners. It is important to be perceived as elegant, modern and trustful. Please check jpg references.

Target Market(s)

Velirande primary clients are individuals, couples and affinity groups of high-net-worth who travel for leisure at least once per year. Seeking the ultimate travel experience, the target clients demand the finest quality activities and accommodations accompanied by a superior level of service.

Industry/Entity Type

Travel Industry

Contact Information for Business Card

Liliana Quesada
- liliana@velirande-mail.example
- +55 11 98437.5216
- velirande-mail.example
- unique travel experiences (we would like to see this signature printed as a detail)

Font styles to use
Sans Serif

Colors

Designer to choose colors to be used in the design.

Requirements
Must have
• the Velirande logo that I have attached
Nice to have
• we would like to have some nice detail, something different that shows that we care about,... we are detail oriented.
Should not have
• decorative fonts

```html
<!DOCTYPE html>
<html lang="en">
<head>
<meta charset="utf-8">
<title>Velirande — Business Card</title>
<link href="https://fonts.googleapis.com/css2?family=Lato:wght@300;400&display=swap" rel="stylesheet">
<style>
  :root {
    --backdrop: #2b2b2b;
    --silver-light: #f7f7f7;
    --silver-mid: #cfcfcf;
    --silver-dark: #a9a7a8;
    --ink: #141414;
  }
  * { box-sizing: border-box; margin: 0; padding: 0; }
  html, body { width: 1200px; height: 900px; overflow: hidden; }
  body {
    background: var(--backdrop);
    font-family: "Lato", sans-serif;
    color: var(--ink);
    display: flex;
    flex-direction: column;
    align-items: center;
    justify-content: center;
    gap: 40px;
  }
  .card {
    width: 700px;
    height: 400px;
    position: relative;
    background: linear-gradient(180deg,
      var(--silver-dark) 0%,
      var(--silver-light) 22%,
      var(--silver-mid) 40%,
      var(--silver-light) 58%,
      var(--silver-dark) 78%,
      var(--silver-light) 100%);
  }
  .card-front {
    display: flex;
    flex-direction: column;
    align-items: center;
    justify-content: center;
  }
  .front-brand {
    font-weight: 400;
    font-size: 44px;
    letter-spacing: 12px;
    margin-top: 40px;
  }
  .tagline {
    position: absolute;
    bottom: 58px;
    left: 0; right: 0;
    text-align: center;
    font-size: 17px;
    letter-spacing: 1.5px;
    font-weight: 400;
  }
  .card-back {
    display: flex;
    align-items: center;
  }
  .back-brand {
    width: 360px;
    text-align: center;
    font-weight: 300;
    font-size: 30px;
    letter-spacing: 11px;
  }
  .divider {
    width: 2px;
    height: 134px;
    background: var(--ink);
  }
  .contact {
    padding-left: 44px;
  }
  .contact-name {
    font-size: 28px;
    font-weight: 400;
    margin-bottom: 14px;
  }
  .contact-list { list-style: none; }
  .contact-list li {
    display: flex;
    align-items: center;
    gap: 14px;
    font-size: 19px;
    line-height: 28px;
  }
  .contact-list svg { width: 16px; height: 16px; flex: none; fill: var(--ink); }
</style>
</head>
<body>
  <section class="card card-front">
    <div class="front-brand">VELIRANDE</div>
    <p class="tagline">UNIQUE TRAVEL EXPERIENCES</p>
  </section>

  <section class="card card-back">
    <div class="back-brand">VELIRANDE</div>
    <div class="divider"></div>
    <div class="contact">
      <h1 class="contact-name">Liliana Quesada</h1>
      <ul class="contact-list">
        <li>
          <svg viewBox="0 0 16 16" aria-hidden="true"><path d="M3.2 1 5.6 3.6 4.4 5.6c.9 2.3 3.3 4.6 6 6l2-1.2L15 12.8 13.6 15C7 14.4 1.6 9 1 2.4Z"/></svg>
          +55 11 98437.5216
        </li>
        <li>
          <svg viewBox="0 0 16 16" aria-hidden="true"><path d="M1 3h14v10H1Zm1.4 1.2L8 8.6l5.6-4.4Z"/></svg>
          liliana@velirande-mail.example
        </li>
        <li>
          <svg viewBox="0 0 16 16" aria-hidden="true"><circle cx="8" cy="8" r="6.5" fill="none" stroke="#141414" stroke-width="1.4"/><ellipse cx="8" cy="8" rx="2.8" ry="6.5" fill="none" stroke="#141414" stroke-width="1.2"/><path d="M1.5 8h13" stroke="#141414" stroke-width="1.2"/></svg>
          www.velirande-mail.example
        </li>
      </ul>
    </div>
  </section>
</body>
</html>
```